Software as a Service to manage Home Care Management

We need a web site designed for Home Care Management Software as a Service product, that facilitates Home Care organizations to manage and schedule carers to visit client homes. We want a modern look and feel using our existing logo.

Target Market(s)

Home Care Management organizations. Product is similar to: https://kelvantro.co/

Coding

Coded - Design and coding required

Number of Pages Required

3 page

```html
<!DOCTYPE html>
<html lang="en">
<head>
<meta charset="utf-8">
<title>Tendrola Care – Home Care Management Software</title>
<link rel="stylesheet" href="https://fonts.googleapis.com/css2?family=Libre+Baskerville:wght@400;700&family=Rubik:wght@300;400;500&display=swap">
<style>
:root{
  --pink:#f0427c;
  --ink:#1b1b1b;
  --text:#333;
  --muted:#8a8a8a;
  --dark:#1f2230;
  --footer:#232323;
  --band:#efefef;
  --white:#fff;
}
*{margin:0;padding:0;box-sizing:border-box}
html,body{width:1200px;height:3937px;overflow:hidden}
body{position:relative;background:var(--white);font-family:"Rubik",sans-serif;color:var(--text)}
.abs{position:absolute}
.serif{font-family:"Libre Baskerville",serif}
.btn{position:absolute;background:var(--pink);color:var(--white);font:500 10px "Rubik",sans-serif;letter-spacing:.5px;display:flex;align-items:center;justify-content:center;text-transform:uppercase}
.pink{color:var(--pink)}
/* header */
.topbar{left:0;top:0;width:1200px;height:11px;background:#111}
.phone-tab{left:0;top:0}
.top-phone{left:1016px;top:10px;color:#fff;font-size:11px}
.brand{display:flex;align-items:center;gap:8px;font-family:"Libre Baskerville",serif;font-size:19px;color:var(--ink);letter-spacing:.5px}
.brand-dot{width:26px;height:26px;border-radius:50%;background:var(--pink)}
.nav{top:44px;font-size:11px;color:var(--ink)}
/* hero */
.hero-photo{left:0;top:66px;width:1200px;height:540px;background:linear-gradient(90deg,#f6f3f0 0%,#ece6e2 40%,#cfc6c2 65%,#b6aca9 100%)}
.hero-sub{left:93px;top:210px;font-size:24px;color:var(--ink)}
.hero-title{left:93px;top:240px;font-size:56px;line-height:59px;font-weight:700;color:var(--ink)}
.hero-title .lite{font-weight:400}
.hero-copy{left:93px;top:366px;font-size:12px;line-height:19px;color:var(--ink);width:330px}
/* welcome */
.welcome-photo{left:93px;top:663px;width:420px;height:455px;background:linear-gradient(135deg,#7a7a7a,#3d3d3d)}
.device{left:469px;top:714px;width:205px;height:404px;border-radius:26px;background:#2a2a2a}
.device-screen{left:12px;top:50px;width:181px;height:296px;background:linear-gradient(#1f7f8e 0 26px,#f4f6f7 26px)}
.eyebrow{font-size:10px;color:var(--pink)}
.h2{font-size:38px;color:var(--ink)}
.para{font-size:11.5px;line-height:18px;color:var(--muted)}
/* happy */
.happy{left:0;top:1182px;width:1200px;height:376px;background:linear-gradient(90deg,#2d2d2d,#4b4b4b 50%,#2f2f2f)}
.band{left:0;top:1558px;width:1200px;height:307px;background:var(--band)}
.card{position:absolute;top:1518px;width:329px;height:297px;background:#fff;box-shadow:0 2px 10px rgba(0,0,0,.06)}
.card-img{height:230px}
.card-label{position:absolute;left:14px;top:254px;font-size:14px;color:var(--ink)}
.card .btn{left:219px;top:248px;width:93px;height:32px}
/* products */
.center{left:0;width:1200px;text-align:center}
.prod{position:absolute;top:2000px;width:220px;text-align:center}
.ring{width:92px;height:92px;border-radius:50%;border:2px solid #f6a7c1;margin:0 auto;display:flex;align-items:center;justify-content:center}
.ring span{width:74px;height:74px;border-radius:50%;background:var(--pink);display:flex;align-items:center;justify-content:center}
.prod h4{font-weight:400;font-size:14.5px;color:var(--ink);margin-top:22px}
.prod p{font-size:10.5px;line-height:15px;color:var(--muted);margin-top:10px}
.arrow{position:absolute;top:2072px;width:22px;height:22px;border:1px solid #ccc;display:flex;align-items:center;justify-content:center}
/* all in one */
.feature h5{font-weight:400;font-size:16px;color:var(--pink)}
.feature p{font-size:11.5px;line-height:19px;color:var(--muted);margin-top:10px;width:400px}
/* form */
.form-sec{left:0;top:2660px;width:1200px;height:380px;background:radial-gradient(ellipse at center,#3a3d4a 0%,#22242f 60%,#1a1c25 100%)}
.lbl{position:absolute;font-size:10px;color:#8c8f9c}
.field{position:absolute;width:253px;height:32px;background:#fff}
/* blog */
.post{position:absolute;top:3160px;width:329px}
.post-img{height:201px}
.post h4{font-weight:500;font-size:13.5px;color:var(--ink);margin-top:22px;letter-spacing:.3px}
.post p{font-size:11px;line-height:17px;color:var(--muted);margin-top:14px}
.post .btn{position:relative;margin-top:22px;width:94px;height:31px}
/* footer */
.footer{left:0;top:3565px;width:1200px;height:372px;background:var(--footer)}
.fcol{position:absolute;top:3628px;font-size:11px;color:#aaa}
.fcol h6{font-size:12px;font-weight:500;color:#fff;margin-bottom:13px;letter-spacing:.3px}
.fcol li{list-style:none;line-height:22.5px}
.soc{position:absolute;top:3702px;width:26px;height:26px;border-radius:50%;background:#3a3a3a}
</style>
</head>
<body>

<!-- header -->
<div class="abs topbar"></div>
<svg class="abs phone-tab" width="1200" height="66" viewBox="0 0 1200 66">
  <path d="M0 11 H930 C960 11 975 30 1005 30 H1200 V66 H0 Z" fill="#fff"/>
</svg>
<div class="abs top-phone">+2 (555) 240 7300</div>
<div class="abs brand" style="left:95px;top:18px"><span class="brand-dot"></span>Tendrola Care</div>
<div class="abs nav pink" style="left:717px">Home</div>
<div class="abs nav" style="left:790px">About Us</div>
<div class="abs nav" style="left:880px">Services</div>
<div class="abs nav" style="left:966px">Products</div>
<div class="abs nav" style="left:1054px">Contact Us</div>

<!-- hero -->
<div class="abs hero-photo" role="img" aria-label="Carer handing a glass of water to an elderly woman on a sofa"></div>
<svg class="abs" style="left:0;top:540px" width="1200" height="70" viewBox="0 0 1200 70">
  <path d="M0 35 C250 -5 500 5 700 28 C900 50 1050 40 1200 12 V70 H0 Z" fill="#fff"/>
  <path d="M0 35 C250 -5 500 5 700 28 C900 50 1050 40 1200 12 V30 C1050 58 900 66 700 50 C500 30 250 20 0 55 Z" fill="var(--pink)"/>
</svg>
<svg class="abs" style="left:1084px;top:568px" width="30" height="6"><circle cx="3" cy="3" r="2.3" fill="#fff"/><circle cx="11" cy="3" r="2.3" fill="#fff"/><circle cx="19" cy="3" r="2.3" fill="#fff"/></svg>
<div class="abs serif hero-sub">Software As a</div>
<div class="abs serif hero-title">Home <span class="pink">Care</span><br><span class="lite">Management</span></div>
<div class="abs hero-copy">Home Care organizations to manage and schedule carers to visit client homes.</div>
<div class="btn" style="left:93px;top:419px;width:101px;height:34px">Get Started</div>

<!-- welcome -->
<div class="abs welcome-photo" role="img" aria-label="Young carer walking arm in arm with an elderly man"></div>
<div class="abs device">
  <div class="abs device-screen" role="img" aria-label="Mobile app screen showing a carer's daily visit schedule"></div>
</div>
<div class="abs eyebrow" style="left:749px;top:772px">Welcome To</div>
<div class="abs serif h2" style="left:749px;top:786px">Tendrola Care</div>
<div class="abs" style="left:749px;top:830px;font-size:11.5px;color:var(--ink)">There are many variations of passages of Lorem Ipsum available</div>
<div class="abs para" style="left:749px;top:862px;width:360px">Sed ut perspiciatis unde omnis iste natus error sit voluptatem accusantium doloremque laudantium, totam rem aperiam, eaque ipsa quae ab illo inventore veritatis et quasi architecto beatae vitae dicta sunt explicabo. Nemo enim ipsam voluptatem quia voluptas sit aspernatur aut odit aut fugit...</div>
<div class="btn" style="left:749px;top:974px;width:101px;height:32px">Read More</div>

<!-- happy customer -->
<div class="abs happy" role="img" aria-label="Black and white photo of a smiling carer with an elderly man"></div>
<div class="abs center" style="top:1320px;color:#fff;font-size:22px;font-weight:300;letter-spacing:1px">JOIN TENDROLA CARE</div>
<div class="abs center serif" style="top:1350px;color:#fff;font-size:54px;font-weight:700">Happy Customer</div>
<div class="abs band"></div>
<div class="card" style="left:93px">
  <div class="card-img" role="img" aria-label="Smiling elderly couple waving" style="background:linear-gradient(135deg,#9bb08a,#c9c0a4)"></div>
  <div class="card-label"><span class="pink">96%</span> Customer Support</div>
  <div class="btn">Read More</div>
</div>
<div class="card" style="left:436px">
  <div class="card-img" role="img" aria-label="Elderly woman holding a mug" style="background:linear-gradient(135deg,#3b2d22,#a07b58)"></div>
  <div class="card-label"><span class="pink">13M</span> Total Care Hours</div>
  <div class="btn">Read More</div>
</div>
<div class="card" style="left:778px">
  <div class="card-img" role="img" aria-label="Nurse kneeling beside an elderly woman with a walker" style="background:linear-gradient(135deg,#c98565,#8fa4c4)"></div>
  <div class="card-label"><span class="pink">17K</span> Active Nurse Body</div>
  <div class="btn">Read More</div>
</div>

<!-- featured products -->
<div class="abs center serif" style="top:1920px;font-size:38px;color:var(--ink)">Featured <b>Products</b></div>
<div class="arrow" style="left:36px"><svg width="8" height="8"><path d="M5.5 1 L2.5 4 L5.5 7" stroke="#333" fill="none"/></svg></div>
<div class="arrow" style="left:1142px"><svg width="8" height="8"><path d="M2.5 1 L5.5 4 L2.5 7" stroke="#333" fill="none"/></svg></div>
<div class="prod" style="left:112px">
  <div class="ring"><span><svg width="40" height="40" viewBox="0 0 40 40" fill="none" stroke="#fff" stroke-width="2"><rect x="6" y="9" width="28" height="24" rx="2"/><path d="M6 16H34M13 5V12M27 5V12"/><path d="M14 22h4M22 22h4M14 27h4"/></svg></span></div>
  <h4>Scheduling / Roster</h4>
  <p>At vero eos et accusamus et iusto odio dignissimos ducimus...</p>
</div>
<div class="prod" style="left:364px">
  <div class="ring"><span><svg width="40" height="40" viewBox="0 0 40 40" fill="none" stroke="#fff" stroke-width="2"><rect x="6" y="8" width="28" height="20" rx="2"/><path d="M16 34h8M20 28v6M20 12v12M14 18h12"/></svg></span></div>
  <h4>Digital Care Plans</h4>
  <p>At vero eos et accusamus et iusto odio dignissimos ducimus...</p>
</div>
<div class="prod" style="left:616px">
  <div class="ring"><span><svg width="40" height="40" viewBox="0 0 40 40" fill="none" stroke="#fff" stroke-width="2"><path d="M5 20L20 7L35 20M10 16V33H30V16"/><circle cx="17" cy="22" r="2.5"/><path d="M17 25v6M23 24v7"/></svg></span></div>
  <h4>Kelvantro eMAR</h4>
  <p>At vero eos et accusamus et iusto odio dignissimos ducimus...</p>
</div>
<div class="prod" style="left:870px">
  <div class="ring"><span><svg width="40" height="40" viewBox="0 0 40 40" fill="none" stroke="#fff" stroke-width="2"><rect x="8" y="6" width="24" height="22" rx="2"/><circle cx="20" cy="16" r="4"/><path d="M12 34h16M20 28v6"/></svg></span></div>
  <h4>Call Monitoring</h4>
  <p>At vero eos et accusamus et iusto odio dignissimos ducimus...</p>
</div>

<!-- all in one -->
<div class="abs serif" style="left:93px;top:2247px;font-size:38px;color:var(--ink)">The All-in-<b>One</b> system</div>
<div class="abs feature" style="left:93px;top:2314px"><h5>Managers</h5><p>Sed ut perspiciatis unde omnis iste natus error sit voluptatem accusantium doloremque laudantium</p></div>
<div class="abs feature" style="left:93px;top:2413px"><h5>Carers</h5><p>Sed ut perspiciatis unde omnis iste natus error sit voluptatem accusantium doloremque laudantium</p></div>
<div class="abs feature" style="left:93px;top:2514px"><h5>Clients And Family</h5><p>Sed ut perspiciatis unde omnis iste natus error sit voluptatem accusantium doloremque laudantium</p></div>
<div class="abs" role="img" aria-label="Black and white photo of an elderly man seated with a cane" style="left:749px;top:2228px;width:358px;height:368px;background:linear-gradient(135deg,#a9a9a9,#4a4a4a)"></div>
<div class="abs" style="left:659px;top:2248px;width:176px;height:348px;border-radius:24px;background:#f4f4f4;border:2px solid #ddd">
  <div class="abs" role="img" aria-label="Mobile app screen showing visit details for a client" style="left:8px;top:42px;width:156px;height:262px;background:linear-gradient(#5d5ae0 0 96px,#fff 96px 238px,#3cc9d0 238px)"></div>
</div>

<!-- form -->
<div class="abs form-sec"></div>
<div class="abs center serif" style="top:2716px;font-size:38px;color:#fff">Want to <b>Know More?</b></div>
<div class="abs center" style="top:2763px;font-size:11px;color:#9a9daa">But I must explain to you how all this mistaken idea of denouncing pleasure</div>
<div class="lbl" style="left:216px;top:2822px">Name:</div>
<div class="lbl" style="left:474px;top:2822px">Email:</div>
<div class="lbl" style="left:731px;top:2822px">Phone:</div>
<div class="field" style="left:216px;top:2839px"></div>
<div class="field" style="left:474px;top:2839px"></div>
<div class="field" style="left:731px;top:2839px"></div>
<div class="lbl" style="left:216px;top:2878px">Company Name:</div>
<div class="lbl" style="left:474px;top:2878px">Demo Date:</div>
<div class="lbl" style="left:731px;top:2878px">Time:</div>
<div class="field" style="left:216px;top:2894px"></div>
<div class="field" style="left:474px;top:2894px"></div>
<div class="field" style="left:731px;top:2894px;font-size:10px;color:#aaa;padding:10px 10px">Please Select
  <svg class="abs" style="right:12px;top:13px" width="8" height="5"><path d="M0 0H8L4 5Z" fill="#888"/></svg></div>
<div class="btn" style="left:216px;top:2940px;width:767px;height:34px">Book Now</div>

<!-- blog -->
<div class="abs center serif" style="top:3093px;font-size:38px;color:var(--ink)">Recent <b>Blog</b></div>
<div class="post" style="left:93px">
  <div class="post-img" role="img" aria-label="Carer holding an elderly person's hands with a small ball" style="background:linear-gradient(135deg,#b98a60,#3f3a3a)"></div>
  <h4>THE STANDARD CHUNK OF LOREM IPSUM</h4>
  <p>Sed ut perspiciatis unde omnis iste natus error sit voluptatem accusantium doloremque laudantium, totam rem aperiam</p>
  <div class="btn">Read More</div>
</div>
<div class="post" style="left:436px">
  <div class="post-img" role="img" aria-label="Elderly woman laughing with a carer" style="background:linear-gradient(135deg,#8c8c8c,#3b3b3b)"></div>
  <h4>THE STANDARD CHUNK OF LOREM IPSUM</h4>
  <p>Sed ut perspiciatis unde omnis iste natus error sit voluptatem accusantium doloremque laudantium, totam rem aperiam</p>
  <div class="btn">Read More</div>
</div>
<div class="post" style="left:778px">
  <div class="post-img" role="img" aria-label="Elderly woman sitting by a bright window" style="background:linear-gradient(135deg,#e4ddd2,#b9a797)"></div>
  <h4>THE STANDARD CHUNK OF LOREM IPSUM</h4>
  <p>Sed ut perspiciatis unde omnis iste natus error sit voluptatem accusantium doloremque laudantium, totam rem aperiam</p>
  <div class="btn">Read More</div>
</div>

<!-- footer -->
<div class="abs footer"></div>
<div class="fcol" style="left:93px"><h6>SITEMAP</h6><ul><li>Home</li><li>About Us</li><li>Services</li><li>Products</li><li>Contact Us</li></ul></div>
<div class="fcol" style="left:240px"><h6>PRODUCTS</h6><ul><li>Scheduling / Roster</li><li>Digital Care plans</li><li>Kelvantro eMAR</li><li>Call monitoring</li><li class="pink">Read More</li></ul></div>
<div class="fcol" style="left:419px"><h6>SYSTEM</h6><ul><li>Sign up</li><li>Prepare &amp; Switch</li><li>Go Live</li></ul></div>
<div class="fcol" style="left:585px"><h6>CONTACTS</h6>
  <div style="display:flex;gap:6px;line-height:16px"><svg width="9" height="12" viewBox="0 0 9 12" style="margin-top:2px"><path d="M4.5 0A4.5 4.5 0 0 0 0 4.5C0 8 4.5 12 4.5 12S9 8 9 4.5A4.5 4.5 0 0 0 4.5 0Z" fill="var(--pink)"/><circle cx="4.5" cy="4.5" r="1.6" fill="var(--footer)"/></svg><span>74 Larkspur Lane, Suite 12<br>Brenmoor 48210 USA</span></div>
  <div style="display:flex;gap:6px;margin-top:18px"><svg width="10" height="12" viewBox="0 0 10 12"><path d="M2 0L4 3L3 4.5C3.6 6.2 5 7.8 6.5 8.6L8 7.5L10 10L8.5 12C4 11 0.5 6.5 0 2Z" fill="var(--pink)"/></svg>+2 (555) 240 7300</div>
  <div style="display:flex;gap:6px;margin-top:22px;align-items:center"><svg width="11" height="8"><rect width="11" height="8" fill="var(--pink)"/><path d="M0 0L5.5 4.5L11 0" stroke="var(--footer)" fill="none"/></svg>info@tendrolacare.com</div>
</div>
<div class="abs brand" style="left:930px;top:3640px;color:#fff;font-size:18px"><span class="brand-dot"></span>Tendrola Care</div>
<div class="soc" style="left:1001px"></div>
<div class="soc" style="left:1039px"></div>
<div class="soc" style="left:1077px"></div>
<div class="abs" style="right:93px;top:3743px;font-size:10px;color:#888">Copyright © 2020 <span style="color:#fff">Tendrola Care</span>. All rights reserved.</div>
<div class="abs" style="left:93px;top:3812px;width:1014px;height:1px;background:#3a3a3a"></div>
<div class="abs" style="left:93px;top:3834px;width:1014px;font-size:8px;line-height:13px;color:#4b4b4b;text-align:center">Our care tools help home care teams plan visits, track hours and share notes with families in one place. Every schedule is kept secure, every carer stays informed, and every client receives the attention they deserve each day, with simple reports for managers.</div>
<div class="abs" style="left:0;top:3930px;width:1200px;height:7px;background:var(--pink)"></div>
<svg class="abs" style="left:0;top:3904px" width="240" height="33" viewBox="0 0 240 33"><path d="M0 0H175C200 0 210 26 240 26V33H0Z" fill="var(--pink)"/></svg>
<div class="abs" style="left:94px;top:3915px;font-size:10px;color:#fff;display:flex;gap:8px;align-items:center;font-weight:500">
  <svg width="16" height="12" viewBox="0 0 16 12" fill="none" stroke="#fff" stroke-width="1.3"><path d="M1 1H11V8H5L2 10V8H1Z"/><path d="M12 4H15V10H14V12L11.5 10H7"/></svg>CHAT WITH US</div>

</body>
</html>
```